TK Business Card

Design a vertical orientation business card with approved logo and fonts (Jubilee Lines and Aviano). Use metallic gold and black, embossing parts of the logo.
Perhaps color back of card black?
Address:
1187 Holloway Crescent
Level 2
West Palm Beach FL 33872

Delphine Marsh
Managing Partner

```html
<!DOCTYPE html>
<html lang="en">
<head>
<meta charset="utf-8">
<title>TK Business Card</title>
<link rel="stylesheet" href="https://fonts.googleapis.com/css2?family=Arimo:wght@400;700&family=Cormorant+SC:wght@500&family=Old+Standard+TT:wght@700&display=swap">
<style>
  :root {
    --backdrop: #d3d3d5;
    --gold-light: #f3d77a;
    --gold: #c9a23a;
    --gold-deep: #8a6a1c;
    --ink: #111111;
    --paper: #ffffff;
    --text-dark: #1a1a1a;
  }
  html, body {
    margin: 0;
    width: 883px;
    height: 1200px;
    overflow: hidden;
    background: var(--backdrop);
  }
  .business-card {
    position: absolute;
    left: 221px;
    top: 206px;
    width: 440px;
    height: 788px;
    box-sizing: border-box;
    padding: 20px;
    background: linear-gradient(160deg, var(--gold-light) 0%, var(--gold) 35%, var(--gold-deep) 60%, var(--gold) 80%, var(--gold-light) 100%);
    box-shadow: 0 2px 6px rgba(0,0,0,0.25);
  }
  .card-frame {
    width: 100%;
    height: 100%;
    box-sizing: border-box;
    border: 24px solid var(--ink);
    background: var(--paper);
    display: flex;
    flex-direction: column;
    align-items: center;
    text-align: center;
  }
  .brand-mark {
    margin-top: 92px;
    display: flex;
    align-items: center;
    gap: 16px;
  }
  .brand-square {
    width: 64px;
    height: 64px;
    background: var(--ink);
  }
  .brand-initials {
    font-family: "Old Standard TT", serif;
    font-weight: 700;
    font-size: 76px;
    line-height: 1;
    color: var(--gold);
  }
  .studio-name {
    margin: 72px 0 0;
    font-family: "Old Standard TT", serif;
    font-weight: 700;
    font-size: 40px;
    letter-spacing: 0.5px;
    line-height: 1;
    color: var(--text-dark);
    white-space: nowrap;
  }
  .studio-tagline {
    margin: 10px 0 0;
    font-family: "Cormorant SC", serif;
    font-weight: 500;
    font-size: 34px;
    letter-spacing: 1.5px;
    line-height: 1;
    color: var(--text-dark);
  }
  .person-name {
    margin: 58px 0 0;
    font-family: "Arimo", sans-serif;
    font-weight: 700;
    font-size: 26px;
    line-height: 1;
    color: var(--gold);
  }
  .person-role {
    margin: 8px 0 0;
    font-family: "Arimo", sans-serif;
    font-size: 17px;
    color: var(--text-dark);
  }
  .studio-address {
    margin: 96px 0 0;
    font-family: "Arimo", sans-serif;
    font-style: normal;
    font-size: 20px;
    line-height: 1.6;
    color: var(--text-dark);
  }
</style>
</head>
<body>
  <section class="business-card">
    <div class="card-frame">
      <div class="brand-mark">
        <span class="brand-square"></span>
        <span class="brand-initials">TK</span>
      </div>
      <h1 class="studio-name">TALLIS KENT</h1>
      <p class="studio-tagline">Design Studio</p>
      <h2 class="person-name">Delphine Marsh</h2>
      <p class="person-role">Managing Partner</p>
      <address class="studio-address">
        1187 Holloway Crescent<br>
        Level 2<br>
        West Palm Beach FL 33872
      </address>
    </div>
  </section>
</body>
</html>
```